Modern, Clean, Edgy & Fun Comedy Show Flyer

We need to a create a new flyer for the comedy show, Harbor Laugh Nights. The original version of the flyer is attached (file: Old flyer), as well as two versions of the logo.
- The text should be the same except now the show is Every First Wednesday and the next show is June 1.
- Remove the jerk shop logo
- Remove the picture of the man, and replace it with a photo of Dale (our host), the Audience, or something of your own design.
* pictures of Dale and the Audience is attached.
* We'd like to keep the same color palette and have also attached a color palette for reference

I have also attached 4 references of flyers that I like, that you can use to get an idea of the theme and aesthetic we are looking for.
* Files: Reference 1, Reference 2, Reference 3, Reference 4
Updates

Colors
3277b5
85acd3
0455a3
eaf1f7
cee9f5
ecf7fb
d5d5d5
e6e6e6

Requirements
Must have
• The harbor laugh nights logo attached
• The text as specified in the project description
• An option with Dale and without

```html
<!DOCTYPE html>
<html lang="en">
<head>
<meta charset="utf-8">
<title>Harbor Laugh Nights – Comedy Show Flyer</title>
<link rel="stylesheet" href="https://fonts.googleapis.com/css2?family=Anton&family=Oswald:wght@500;700&family=Montserrat:wght@600&display=swap">
<style>
  :root {
    --backdrop: #93b1c2;
    --night: #22243a;
    --night-soft: #34374f;
    --ink: #2b2c38;
    --paper: #f4f7f8;
    --teal: #4fb39a;
    --lavender: #a9a6da;
    --sky: #9cc4da;
    --cyan: #94d9dc;
    --cyan-pale: #cdeef0;
    --violet: #5b5294;
    --rule: #d9dde6;
  }
  * { box-sizing: border-box; margin: 0; padding: 0; }
  html, body { width: 1200px; height: 1200px; overflow: hidden; }
  body { background: var(--backdrop); position: relative; }

  .flyer {
    position: absolute; left: 190px; top: 30px;
    width: 820px; height: 1140px;
    background: var(--paper); overflow: hidden;
    box-shadow: 0 18px 40px rgba(20, 40, 60, .35);
  }
  .stage-backdrop {
    position: absolute; left: 0; top: 0; width: 820px; height: 780px;
    background: radial-gradient(ellipse at 60% 30%, var(--night-soft), var(--night) 70%);
  }
  .info-panel { position: absolute; left: 0; top: 640px; width: 820px; height: 500px; }
  .performer-photo {
    position: absolute; left: 0; top: 740px; width: 470px; height: 400px;
    background: linear-gradient(160deg, #4a3426 0%, #2a1d18 55%, #5a3b2a 100%);
  }

  .venue-line {
    position: absolute; left: 40px; top: 34px;
    font-family: "Montserrat", sans-serif; font-weight: 600;
    font-size: 20px; letter-spacing: 2px; color: #fff;
  }
  .venue-line .venue-name { color: var(--teal); margin-right: 10px; }
  .rule { position: absolute; height: 2px; background: var(--rule); }
  .rule.top { left: 40px; top: 76px; width: 740px; }
  .rule.mid { left: 40px; top: 430px; width: 740px; }

  .show-name {
    position: absolute; left: 40px; top: 200px; width: 270px;
    font-family: "Oswald", sans-serif; font-weight: 700;
    font-size: 44px; line-height: 1.05; color: #fff; text-transform: uppercase;
  }
  .show-title {
    position: absolute; left: 330px; top: 92px;
    font-family: "Anton", sans-serif; color: #f3f3f3; line-height: .95;
  }
  .show-title .line1 { display: block; font-size: 140px; }
  .show-title .line2 { display: block; font-size: 172px; }

  .lineup {
    position: absolute; left: 40px; top: 448px;
    font-family: "Oswald", sans-serif; font-weight: 700;
    font-size: 56px; line-height: 1.08; text-transform: uppercase; letter-spacing: -1px;
  }
  .lineup span { white-space: nowrap; }
  .c-teal { color: var(--teal); }
  .c-lav { color: var(--lavender); }
  .c-sky { color: var(--sky); }

  .details {
    position: absolute; left: 492px; top: 694px; width: 310px;
    font-family: "Anton", sans-serif; text-transform: uppercase; line-height: 1;
  }
  .details p { white-space: nowrap; }
  .details .hosted { font-size: 52px; color: var(--violet); }
  .details .host { font-size: 34px; color: var(--ink); margin-top: 4px; }
  .details .sep { height: 2px; background: var(--violet); margin: 10px 0; }
  .details .first { font-size: 54px; color: var(--violet); }
  .details .day { font-size: 56px; color: var(--ink); }
  .details .month { font-size: 32px; color: var(--violet); margin-top: 4px; }
  .details .next { font-size: 28px; color: var(--ink); margin-top: 6px; }
  .details .entry { font-size: 50px; color: var(--ink); }
  .details .doors { font-size: 36px; color: var(--violet); margin-top: 4px; }
</style>
</head>
<body>
  <main class="flyer">
    <div class="stage-backdrop" role="img" aria-label="Dim photograph of a comedy club stage and audience"></div>

    <svg class="info-panel" viewBox="0 640 820 500" aria-hidden="true">
      <polygon points="0,740 820,640 820,1140 0,1140" fill="var(--cyan-pale)"/>
      <polygon points="430,720 820,640 820,900 560,1140 430,1140" fill="var(--cyan)" opacity=".55"/>
      <polygon points="520,900 820,820 820,1140 470,1140" fill="#ffffff" opacity=".8"/>
    </svg>

    <div class="performer-photo" role="img" aria-label="Photo of a smiling comedian holding a microphone on stage"></div>

    <p class="venue-line"><span class="venue-name">THE TIN LANTERN</span>42 ORCHARD LANE HARBORVIEW</p>
    <div class="rule top"></div>

    <p class="show-name">Harbor Laugh Nights</p>

    <h1 class="show-title"><span class="line1">COMEDY</span><span class="line2">SHOW</span></h1>
    <div class="rule mid"></div>

    <p class="lineup">
      <span><span class="c-teal">Featuring</span> <span class="c-sky">Marcus Bellamy</span></span><br>
      <span><span class="c-lav">Alec Winter</span> <span class="c-teal">Noel Gardenfield</span></span><br>
      <span><span class="c-sky">Nikhil Prasad</span> <span class="c-lav">Gemma Yardley</span></span>
    </p>

    <section class="details">
      <p class="hosted">Hosted by</p>
      <p class="host">Dale Cobbins</p>
      <div class="sep"></div>
      <p class="first">The First</p>
      <p class="day">Wednesday</p>
      <p class="month">Of Every Month</p>
      <p class="next">Next Show June 1</p>
      <div class="sep"></div>
      <p class="entry">Free Entry</p>
      <p class="doors">Open 630PM</p>
    </section>
  </main>
</body>
</html>
```